" Somos um grupo de Psiquiatras que atende em domicílio e hospitais. Funcionamos em escala de sobreaviso. Normalmente fazemos visitas para pacientes que por alguma limitação ou urgência não podem ser atendidos em consultório. "

```html
<!DOCTYPE html>
<html lang="pt-BR">
<head>
<meta charset="utf-8">
<title>Grupo Sereno – Cartão de visita</title>
<link href="https://fonts.googleapis.com/css2?family=Open+Sans:wght@400;600&display=swap" rel="stylesheet">
<style>
  :root {
    --bg: #ecebe8;
    --card: #666667;
    --text: #ffffff;
    --muted: #d9d9d9;
    --accent: #5cc6cf;
    --accent-dark: #2a9aa5;
    --faint: rgba(255,255,255,0.12);
  }
  * { margin: 0; padding: 0; box-sizing: border-box; }
  html, body {
    width: 1200px; height: 1200px; overflow: hidden;
    background: var(--bg);
    font-family: "Open Sans", Arial, sans-serif;
  }
  .stage { position: relative; width: 1200px; height: 1200px; }
  .card {
    position: absolute;
    width: 668px; height: 374px;
    background: var(--card);
    color: var(--text);
    box-shadow: 0 10px 24px rgba(0,0,0,0.25);
    overflow: hidden;
  }
  /* Back of card: team list */
  .card-back { left: 319px; top: 144px; }
  .team-list { list-style: none; position: absolute; left: 84px; top: 86px; }
  .team-list li { font-size: 18px; line-height: 47px; color: var(--text); }
  .side-accent {
    position: absolute; right: 0; top: 60px;
    width: 14px; height: 252px;
    background: linear-gradient(180deg, var(--accent), var(--accent-dark));
  }
  .faint-circle {
    position: absolute; right: 70px; top: 150px;
    width: 150px; height: 150px;
    border: 3px solid var(--faint); border-radius: 50%;
  }
  /* Front of card: brand + service */
  .card-front { left: 235px; top: 643px; }
  .brand {
    position: absolute; left: 0; width: 334px; top: 120px;
    text-align: center;
  }
  .brand-dot {
    display: block; width: 70px; height: 70px; margin: 0 auto 14px;
    border-radius: 50%; border: 4px solid var(--accent);
  }
  .brand-name {
    font-size: 30px; font-weight: 400; letter-spacing: 2px;
    text-transform: uppercase; color: var(--text);
  }
  .brand-tagline {
    margin-top: 4px; font-size: 11px; letter-spacing: 2.5px;
    text-transform: uppercase; color: var(--accent);
  }
  .divider {
    position: absolute; left: 334px; top: 96px;
    width: 2px; height: 180px; background: var(--muted);
  }
  .service {
    position: absolute; left: 389px; top: 130px;
    font-size: 24px; line-height: 36px; color: var(--text);
  }
  .service .phone { font-size: 21px; }
  .bottom-accent {
    position: absolute; left: 0; bottom: 0;
    width: 100%; height: 14px;
    background: linear-gradient(90deg, var(--accent-dark), var(--accent));
  }
</style>
</head>
<body>
<main class="stage">
  <section class="card card-back">
    <ul class="team-list">
      <li>Dra. Helena Moura Cavalcanti - CRM 40817</li>
      <li>Dra. Lívia Tavares - CRM 36204</li>
      <li>Dr. Rafael Siqueira - CRM 39512</li>
      <li>Dra. Beatriz Fontes - CRM 37148</li>
      <li>Dr. Otávio Brandão - CRM 38625</li>
    </ul>
    <span class="faint-circle"></span>
    <span class="side-accent"></span>
  </section>

  <section class="card card-front">
    <div class="brand">
      <span class="brand-dot"></span>
      <div class="brand-name">Grupo Sereno</div>
      <div class="brand-tagline">Cuidados em Psiquiatria</div>
    </div>
    <span class="divider"></span>
    <div class="service">
      <p>Atendimento</p>
      <p>hospitalar e domiciliar</p>
      <p class="phone">(81) 9 9000.4812</p>
    </div>
    <span class="bottom-accent"></span>
  </section>
</main>
</body>
</html>
```